Business card design needed

I am a business consultant but I call myself an "organizational leadership consultant." My clients hire me to do organizational development work in the areas of leadership development, strategic planning, shared visioning, governance (bylaws, policy, board development), collaborative capacity building, and organizational communications. I work in numerous sectors (public, private, not-for-profit and governmental) but most of my clients are in not-for-profit (but not human service - think national advocacy organizations, student governments, regulatory colleges, and professional (accreditation) bodies).

I want my cards to convey the concepts of being reliable and smart (of course) but also vibrant and signifying new beginnings/possibilities.

I am uploading a copy of a logo I have used for some time (adapted from QV logo free website). I like the hues of the primary colours used, its symmetrical, and that it has movement. I am open to a new logo (but not essential) with these same qualities: I really like fractals BTW.

I think one of the most beautiful creatures on earth is the harlequin duck, but have not been able to figure out how to incorporate that into my brand. Mostly what I love is the colours and how they appear on the duck. I am sharing that just as an idea in case your creative energy is leaning toward creating a new design rather than working with my logo.

If I had the right business card to start with, I might consider re-branding and working that into my digital and print materials. I realize this is against the use of RGBY in my current logo.
Updates

Hi - I forgot to mention to please use the RTVP Certified patch/logo as a just a small feature of the card - it is not my main logo. Also, I like fonts that are clean.  Thanks!

Target Market(s)

Higher level business professionals

Industry/Entity Type

Business Consultant

Contact Information for Business Card

Moira Castellane, MA, BSc, RTVP(pls insert trademark symbol)
Organizational Leadership Consultant
250-487-6190
moira@mcastellaneadvisory.example
www.mcastellaneadvisory.example
Marrow Cove, NS

Logo Text

Leadership Consulting for a New Future

Logo styles of interest
Emblem Logo
Abstract Logo
Requirements
Must have
• Must have:
1. Name of my business (Moira Castellane Consulting) and contact info per above
2. My logo (or your new idea for a logo) with a my tagline somewhere (tagline can be on back. Tagline is "Leadership Consulting for a New Future)
3. RTVP certified logo (attachment #3)
3. Chirpline logo with my acct name (@moiracastellane), and
4. Workweave logo
Should not have
• I don't like the "solid" primary colours as in those found on brikko or in a poppets box - transparency in those colours is acceptable.

Do not include images of people shaking hands or other corny 'business' imagery.;-)

```html
<!DOCTYPE html>
<html lang="en">
<head>
<meta charset="utf-8">
<title>Moira Castellane Consulting – Business Card</title>
<link rel="stylesheet" href="https://fonts.googleapis.com/css2?family=Arimo:wght@400;700&display=swap">
<style>
  :root {
    --brand-blue: #3a7fb0;
    --ink: #111111;
    --paper: #ffffff;
    --mark-tint: #e6eff6;
    --badge-orange: #e8692a;
    --faint-tint: #f3f1ea;
  }
  * { margin: 0; padding: 0; box-sizing: border-box; }
  html, body { width: 1200px; height: 693px; overflow: hidden; background: var(--paper); }
  .card {
    position: relative;
    width: 1200px;
    height: 693px;
    background: var(--paper);
    font-family: "Arimo", Arial, sans-serif;
    overflow: hidden;
  }
  .card > * { position: absolute; line-height: 1.15; }
  .faint-decoration { right: -60px; bottom: -70px; }
  .brand-mark { left: 45px; top: 47px; }
  .brand-mark-name {
    left: 45px; top: 47px; width: 382px; height: 382px;
    display: flex; align-items: center; justify-content: center;
    font-size: 40px; font-weight: 700; color: var(--brand-blue);
  }
  .right-block { right: 48px; text-align: right; white-space: nowrap; }
  .company-name { top: 66px; font-size: 52px; font-weight: 700; color: var(--brand-blue); }
  .person-name { top: 182px; font-size: 35px; color: var(--ink); }
  .person-name .credentials { font-size: 29px; }
  .role { top: 255px; font-size: 31px; font-weight: 700; color: var(--brand-blue); }
  .contact { top: 330px; font-size: 27px; color: var(--ink); }
  .social-name-chirp {
    left: 60px; top: 478px; font-size: 23px; font-weight: 700; color: var(--brand-blue);
  }
  .social-handle { left: 194px; top: 463px; font-size: 45px; color: var(--ink); white-space: nowrap; }
  .social-name-weave {
    left: 672px; top: 458px; font-size: 52px; font-weight: 700; color: var(--ink);
  }
  .tagline { left: 64px; top: 566px; font-size: 49px; font-weight: 700; color: var(--brand-blue); white-space: nowrap; }
  .web-line { left: 194px; top: 624px; font-size: 20px; color: var(--ink); white-space: nowrap; }
  .cert-badge { left: 1039px; top: 474px; }
</style>
</head>
<body>
  <main class="card">
    <svg class="faint-decoration" width="420" height="420" viewBox="0 0 420 420" aria-hidden="true">
      <circle cx="210" cy="210" r="200" fill="var(--faint-tint)"/>
    </svg>

    <svg class="brand-mark" width="382" height="382" viewBox="0 0 382 382" aria-hidden="true">
      <circle cx="191" cy="191" r="180" fill="var(--mark-tint)"/>
    </svg>
    <div class="brand-mark-name">Castellane</div>

    <h1 class="right-block company-name">Moira Castellane Consulting</h1>
    <p class="right-block person-name">Moira Castellane<span class="credentials">—MA, BSc, RTVP™</span></p>
    <p class="right-block role">Organizational Leadership Consultant</p>
    <p class="right-block contact">(250) 487-6190—moira@mcastellaneadvisory.example</p>

    <span class="social-name-chirp">Chirpline</span>
    <span class="social-handle">@MoiraCastellane</span>
    <span class="social-name-weave">Workweave</span>

    <p class="tagline">Leadership Consulting for a New Future</p>
    <p class="web-line">www.mcastellaneadvisory.example—Marrow Cove, NS</p>

    <svg class="cert-badge" width="115" height="172" viewBox="0 0 115 172" role="img" aria-label="Certification badge">
      <rect x="4" y="4" width="107" height="164" rx="10" fill="var(--badge-orange)" opacity="0.85"/>
    </svg>
  </main>
</body>
</html>
```